Angebotsflyer - nicht Einladung -  für Personalmarketing Agentur
Angebotsflyer - nicht Einladung - für Personalmarketing Agentur
Zielgruppe
Wir sind eine Personalmarketing Agentur, die Unternehmen zu einer starken Arbeitgebermarke verhilft. Achtung: Wir sind keine Personalvermittler. Unternehmen, die als Arbeitgeber sichtbar werden möchten oder die ihre Mitarbeiterzufriedenheit steigern möchten sind unsere Zielgruppe.
Aufgabenstellung
DIN Lang. Wir möchten den Kreativen so viel Gestaltungsraum wie möglich lassen mit der Bitte sich nach unserer Website zu orientieren: www.teamsignal.works
Unser Leistungs-Portfolio sollte ansprechend dargestellt werden:
- Individuelles Recruiting
- Stellenanzeigen
- Mitarbeiterbefragungen
- Was Bewerber wollen
- Karriereseiten
- Mitarbeiter Benefits
- HR digital
- Corporate Fashion
- vUk Akademie (HR Workshops: Personalmarketing, Mitarbeitermotivation und -bindung, Stellenanzeigen, etc.)
vUk steht für value under kindness und für ehrliches Personalmarketing. Dabei ist es essentiell sich zunächst dem internen Personalmarketing zu widmen. Von innen heraus entsteht dann ein stimmiges externes Personalmarketingkonzept, welches von den Mitarbeitern getragen wird.
Gutes Personalmarketing ist mehr als das jährliche Grillfest.

```html
<!DOCTYPE html>
<html lang="de">
<head>
<meta charset="utf-8">
<title>vUk Personalmarketing – Angebotsflyer DIN Lang</title>
<link rel="stylesheet" href="https://fonts.googleapis.com/css2?family=Nunito+Sans:wght@400;600;700;800;900&display=swap">
<style>
  :root {
    --navy: #0f3b55;
    --navy-deep: #0b3550;
    --teal: #2aa2a5;
    --teal-light: #4cbfbf;
    --figure-teal: #25a3a4;
    --white: #ffffff;
    --page: #ececec;
    --font: "Nunito Sans", Arial, sans-serif;
  }
  * { box-sizing: border-box; margin: 0; padding: 0; }
  html, body { width: 1200px; height: 1200px; overflow: hidden; }
  body { background: var(--page); font-family: var(--font); color: var(--navy); position: relative; }

  .card {
    position: absolute; left: 57px; width: 1085px; height: 516px;
    background: var(--white); overflow: hidden;
    box-shadow: 0 6px 18px rgba(0,0,0,0.18);
  }
  .card--front { top: 68px; }
  .card--back { top: 614px; }

  .card__shapes { position: absolute; inset: 0; width: 100%; height: 100%; }

  /* front */
  .hero-title {
    position: absolute; left: 81px; top: 80px;
    font-weight: 800; font-size: 70px; line-height: 65px;
    color: var(--white); letter-spacing: 0.5px; text-transform: uppercase;
  }
  .hero-sub {
    position: absolute; left: 82px; top: 352px;
    font-size: 22px; line-height: 26px; font-weight: 400;
    color: var(--white); letter-spacing: 0.3px;
  }
  .hero-bar { position: absolute; left: 84px; top: 420px; width: 104px; height: 10px; background: var(--white); }

  .brand {
    position: absolute; font-weight: 800; color: var(--navy);
    letter-spacing: -2px; line-height: 1;
  }
  .card--front .brand { left: 845px; top: 48px; font-size: 88px; }
  .card--back .brand { left: 905px; top: 36px; font-size: 66px; }

  /* back */
  .back-title {
    position: absolute; left: 52px; top: 50px;
    font-weight: 800; font-size: 34px; line-height: 36px; text-transform: uppercase;
  }
  .back-tagline { position: absolute; left: 52px; top: 120px; font-size: 20px; font-weight: 400; }
  .back-bar { position: absolute; left: 52px; top: 168px; width: 78px; height: 7px; background: var(--teal-light); }

  .intro {
    position: absolute; left: 52px; top: 200px; width: 205px;
    font-weight: 800; font-size: 16px; line-height: 21px;
  }
  .intro p + p { margin-top: 21px; }

  .column { position: absolute; top: 200px; font-size: 17px; line-height: 20px; }
  .column--benefits { left: 288px; width: 240px; }
  .column--disciplines { left: 539px; width: 220px; }
  .column h3 { font-size: 17px; font-weight: 800; text-transform: uppercase; }
  .column ul { list-style: none; }
  .column li { padding-left: 11px; text-indent: -11px; letter-spacing: 0.3px; }
  .column li::before { content: "- "; }

  .cta {
    position: absolute; right: 52px; top: 294px; text-align: right;
    color: var(--white); font-weight: 800; font-size: 16.5px; line-height: 20px;
    text-transform: uppercase;
  }
  .contact {
    position: absolute; right: 52px; top: 387px; text-align: right;
    color: var(--white); font-size: 13.5px; line-height: 16.5px; letter-spacing: 0.3px;
    font-style: normal;
  }
  .contact strong { font-weight: 800; }
</style>
</head>
<body>

<section class="card card--front">
  <svg class="card__shapes" viewBox="0 0 1085 516" aria-hidden="true">
    <defs>
      <linearGradient id="front-gradient" x1="0" y1="0" x2="1" y2="0.6">
        <stop offset="0" stop-color="#2a9fa3"/>
        <stop offset="0.45" stop-color="#0d4a62"/>
        <stop offset="1" stop-color="#0b3550"/>
      </linearGradient>
    </defs>
    <polygon points="25,26 803,26 775,131 819,187 1058,249 1058,491 25,491" fill="url(#front-gradient)"/>
  </svg>
  <svg class="card__shapes" viewBox="0 0 1085 516" role="img" aria-label="Illustration: ein großer gerüsteter Krieger mit Speer, davor eine kleine helle Figur mit Schleuder">
    <rect x="625" y="26" width="170" height="465" rx="12" fill="var(--figure-teal)"/>
  </svg>

  <h1 class="hero-title">Seien Sie<br>der David<br>unter den<br>Goliaths</h1>
  <p class="hero-sub">EHRLICHES PERSONALMARKTING<br>OUT OF THE BOX</p>
  <div class="hero-bar"></div>
  <div class="brand">vUk</div>
</section>

<section class="card card--back">
  <svg class="card__shapes" viewBox="0 0 1085 516" aria-hidden="true">
    <defs>
      <linearGradient id="back-gradient" x1="0" y1="0" x2="1" y2="1">
        <stop offset="0" stop-color="#0b3550"/>
        <stop offset="0.55" stop-color="#0f4a60"/>
        <stop offset="1" stop-color="#2a9fa3"/>
      </linearGradient>
    </defs>
    <polygon points="806,184 1086,268 1086,516 701,516" fill="url(#back-gradient)"/>
  </svg>

  <h2 class="back-title">Im „War of Talents“ den<br>Sieg für sich verbuchen</h2>
  <p class="back-tagline">vUk | VALUE UNDER KINDNESS</p>
  <div class="back-bar"></div>
  <div class="brand">vUk</div>

  <div class="intro">
    <p>Unmögliches möglich machen. Erzielen Sie mit uns im Wettstreit um die besten Mitarbeiter die Treffer zum Erfolg.</p>
    <p>Wir bieten ehrliches Personalmarketing der Neuzeit und stärken nachhaltig ihre Arbeits­gebermarke - sowohl innen als auch nach Außen.</p>
  </div>

  <div class="column column--benefits">
    <h3>Benefits</h3>
    <ul>
      <li>Arbeitnehmer binden</li>
      <li>Von passenden Bewerbern gefunden werden</li>
      <li>Gesundes Betriebsklima schaffen und daraus resul­tierend Firmenergebnisse verbessern</li>
      <li>Fluktuationen verringern und Planungssicherheit schaffen</li>
    </ul>
  </div>

  <div class="column column--disciplines">
    <h3>Disziplinen</h3>
    <ul>
      <li>Individuelles Recruiting</li>
      <li>Stellenanzeigen</li>
      <li>Mitarbeiterbefragungen</li>
      <li>Was Bewerber wollen</li>
      <li>Karriereseiten</li>
      <li>Mitarbeiter Benefits</li>
      <li>HR digital</li>
      <li>Corporate Fashion</li>
      <li>vUk Akademie*</li>
    </ul>
  </div>

  <p class="cta">Vereinbaren Sie jetzt<br>einen Termin und<br>erhalten Sie eine Stunde<br>Beratung kostenlos.</p>
  <address class="contact">
    <strong>vUk Personalmarketing GmbH</strong><br>
    Lindenweg 27 28195 Bremen<br>
    T.: 0421 55 30 18 42<br>
    info@vuk-team.de<br>
    teamsignal.works
  </address>
</section>

</body>
</html>
```